Mental Health and Marriage & Family Counseling Office Business Card Design

I work with a wide range of emotional and behavioral issues providing services that span from therapy for depression and grief counseling to parenting support, couples counseling and beyond. In a comfortable and supportive atmosphere, I offer a highly personalized approach tailored to each of my clients individual needs to help attain the personal growth they’re striving for. Providing individual, couples and family counseling.
Treatment specialization includes: Therapy for Depression and Anxiety, Couples Counseling, Family Counseling, Parenting Support, Grief Counseling, Work and Career issues, Stress Management, Conflict Resolution. I would like to see designs that use the colors "of a Peacock feather" , such as blues and greens, etc.

Business

Gloria B. Fenmore, MS, LPC
Licensed Professional Counselor
415 Orchard Bend Suite 263
Jacksonville, NC 28517

(910) 555-0147 Fax: (910) 555-0148
www.gloriafenmorelpc.example
gloria@gloriafenmorelpc.example

```html
<!DOCTYPE html>
<html lang="en">
<head>
<meta charset="utf-8">
<title>Gloria B. Fenmore, MS, LPC — Business Card</title>
<link rel="stylesheet" href="https://fonts.googleapis.com/css2?family=Tinos:wght@400;700&family=Didact+Gothic&display=swap">
<style>
  :root {
    --backdrop: #e4e6e6;
    --teal-light: #2fa3a0;
    --teal: #1c8a8e;
    --teal-deep: #14607a;
    --navy: #1d3f66;
    --orange: #f0a13a;
    --cream: #f7f1dc;
    --cream-light: #fdfaf0;
    --ink: #173a5c;
    --name: #1f8f8f;
  }
  * { box-sizing: border-box; margin: 0; padding: 0; }
  html, body { width: 1200px; height: 863px; overflow: hidden; background: var(--backdrop); }
  .canvas {
    width: 1200px; height: 863px;
    display: flex; flex-direction: column; align-items: center; justify-content: center; gap: 52px;
  }
  .card {
    position: relative; width: 595px; height: 340px; border-radius: 18px; overflow: hidden;
    box-shadow: 0 6px 18px rgba(0,0,0,.18);
  }
  .card svg.art { position: absolute; inset: 0; width: 100%; height: 100%; }

  /* front */
  .card-front { background: radial-gradient(ellipse at 40% 40%, var(--teal-light), var(--teal) 45%, var(--teal-deep) 100%); }
  .front-mark {
    position: absolute; left: 0; right: 0; top: 150px; text-align: center;
    font-family: "Tinos", serif; font-weight: 700; font-size: 30px; color: #ffffff; letter-spacing: 1px;
  }

  /* back */
  .card-back { background: linear-gradient(135deg, var(--cream-light), var(--cream)); }
  .back-mark {
    position: absolute; left: 34px; top: 24px;
    font-family: "Tinos", serif; font-weight: 700; font-size: 20px; color: var(--name);
  }
  .identity { position: absolute; left: 34px; top: 58px; width: 390px; }
  .name { font-family: "Tinos", serif; font-weight: 400; font-size: 33px; color: var(--name); line-height: 1.1; white-space: nowrap; }
  .name .credentials { font-size: 18px; }
  .title { font-family: "Didact Gothic", sans-serif; font-size: 17px; color: var(--name); margin-top: 2px; padding-bottom: 8px; border-bottom: 1px solid var(--name); }
  .contact { position: absolute; left: 34px; top: 152px; list-style: none; font-family: "Tinos", serif; font-weight: 700; font-size: 14px; color: var(--ink); }
  .contact li { display: flex; align-items: center; gap: 10px; height: 22px; white-space: nowrap; }
  .contact svg { width: 13px; height: 13px; fill: #8a8f94; flex: none; }
</style>
</head>
<body>
<main class="canvas">

  <section class="card card-front" aria-label="Card front">
    <svg class="art" viewBox="0 0 595 340" preserveAspectRatio="none" aria-hidden="true">
      <polygon points="330,0 395,0 330,62" fill="var(--orange)"/>
      <polygon points="395,0 595,0 595,120 410,92" fill="#1f7f8c" opacity=".7"/>
      <polygon points="410,92 595,120 595,340 470,340" fill="#2a9a97" opacity=".8"/>
      <polygon points="410,92 470,340 300,340" fill="var(--navy)" opacity=".55"/>
      <polygon points="520,250 595,210 595,340 540,340" fill="var(--navy)" opacity=".7"/>
    </svg>
    <div class="front-mark">Fenmore</div>
  </section>

  <section class="card card-back" aria-label="Card back">
    <svg class="art" viewBox="0 0 595 340" preserveAspectRatio="none" aria-hidden="true">
      <polygon points="410,0 595,0 595,150 315,340 300,340" fill="var(--orange)"/>
      <polygon points="370,340 595,188 595,340" fill="var(--teal)"/>
      <polygon points="315,340 595,150 595,188 370,340" fill="#fffdf6"/>
    </svg>

    <div class="back-mark">Fenmore</div>

    <header class="identity">
      <h1 class="name">Gloria B. Fenmore<span class="credentials">, MS, LPC</span></h1>
      <p class="title">Licensed Professional Counselor</p>
    </header>

    <ul class="contact">
      <li><svg viewBox="0 0 16 16"><path d="M8 0a5 5 0 0 0-5 5c0 4 5 11 5 11s5-7 5-11a5 5 0 0 0-5-5zm0 7a2 2 0 1 1 0-4 2 2 0 0 1 0 4z"/></svg>415 Orchard Bend Suite 263 Jacksonville, NC 28517</li>
      <li><svg viewBox="0 0 16 16"><path d="M3 1l3 3-2 2c1 2 3 4 5 5l2-2 3 3-2 3C6 14 2 10 1 3z"/></svg>(910) 555-0147</li>
      <li><svg viewBox="0 0 16 16"><path d="M4 1h7v4H4zM1 6h14v7h-3v2H4v-2H1zm4 5v3h6v-3z"/></svg>(910) 555-0148</li>
      <li><svg viewBox="0 0 16 16"><path d="M8 0a8 8 0 1 0 0 16A8 8 0 0 0 8 0zm0 2c1 1 2 3 2 6s-1 5-2 6c-1-1-2-3-2-6s1-5 2-6zM2 8h12v1H2z"/></svg>www.gloriafenmorelpc.example</li>
      <li><svg viewBox="0 0 16 16"><path d="M0 3h16v10H0zm1 1v1l7 5 7-5V4z"/></svg>gloria@gloriafenmorelpc.example</li>
    </ul>
  </section>

</main>
</body>
</html>
```